Solar accessories banner to produce more green energy

Hello,
we need a banner for a solar accessories page.
https://plovinta.de/index.php/zubehoer/
as we are commissioning the first banner for the entire homepage here, we are open to all directions. The current existing banner is just a random image of the installed theme and should not be a reference.
The banner should be created in a dark style. Our core colors are black / yellow / white.
The banner should have a clear reference to the accessories shown below and consider other accessories such as mounting systems of solar panels, cables, adapters, etc.
I would be happy to answer any queries.
Regards
Malte
-------------------------------------------------- ----------------------------------------------
Hello,
https://plovinta.de/index. php / accessories /
Since we are commissioning the first banner for the entire homepage, we are open to all directions. The currently existing banner is only a random image of the installed theme and is not intended to be a reference.
The banner should be created in a dark stem. Our core colors are black / yellow / white.
The banner should have a clear reference to the accessories shown below and take into account other accessories such as mounting systems for solar panels, cables, adapters, etc.
I am happy to answer any questions.
greetings
Malte

```html
<!DOCTYPE html>
<html lang="de">
<head>
<meta charset="utf-8">
<title>Montage und Anschluss – Zubehör</title>
<link rel="stylesheet" href="https://fonts.googleapis.com/css2?family=Nunito:wght@800;900&family=Roboto:wght@400;700&display=swap">
<style>
  :root {
    --bg: #1b1b1b;
    --bg-soft: #232323;
    --yellow: #ffcb05;
    --white: #ffffff;
    --ink: #1b1b1b;
    --muted: #b9b9b9;
    --product-dark: #262626;
    --product-mid: #4a4a4a;
    --product-light: #f4f4f4;
  }
  * { margin: 0; padding: 0; box-sizing: border-box; }
  html, body { width: 1200px; height: 439px; overflow: hidden; background: var(--bg); }
  .banner {
    position: relative;
    width: 1200px;
    height: 439px;
    overflow: hidden;
    background: var(--bg);
  }
  .banner__shapes {
    position: absolute;
    inset: 0;
  }
  .banner__content {
    position: absolute;
    left: 80px;
    top: 96px;
    width: 420px;
  }
  .banner__title {
    font-family: "Nunito", sans-serif;
    font-weight: 900;
    font-size: 49px;
    line-height: 54px;
    color: var(--white);
    letter-spacing: 0.5px;
  }
  .banner__highlight {
    background: var(--yellow);
    color: var(--ink);
    padding: 0 4px;
  }
  .banner__text {
    margin-top: 14px;
    font-family: "Roboto", sans-serif;
    font-size: 12.5px;
    line-height: 22px;
    color: var(--muted);
  }
  .banner__button {
    position: absolute;
    left: 80px;
    top: 304px;
    width: 373px;
    height: 49px;
    border-radius: 25px;
    background: var(--yellow);
    display: flex;
    align-items: center;
    gap: 13px;
    padding-left: 21px;
    font-family: "Roboto", sans-serif;
    font-weight: 700;
    font-size: 12px;
    letter-spacing: 0.2px;
    color: var(--ink);
    text-decoration: none;
  }
  .banner__button svg { flex: none; }
</style>
</head>
<body>
  <section class="banner">
    <svg class="banner__shapes" width="1200" height="439" viewBox="0 0 1200 439">
      <defs>
        <linearGradient id="product-tone" x1="0" y1="0" x2="1" y2="0.4">
          <stop offset="0" stop-color="var(--product-dark)"/>
          <stop offset="0.4" stop-color="var(--product-mid)"/>
          <stop offset="0.62" stop-color="#9a9a9a"/>
          <stop offset="0.8" stop-color="var(--product-light)"/>
          <stop offset="1" stop-color="#5a5a5a"/>
        </linearGradient>
      </defs>
      <!-- corner accent top left -->
      <path class="corner-accent" d="M0 0 H114 L40 70 Q30 78 18 77 Q0 75 0 58 Z" fill="var(--yellow)"/>
      <!-- soft dark band behind product stage -->
      <rect x="-230" y="-230" width="460" height="460" rx="44" fill="var(--bg-soft)"
            transform="translate(940 110) rotate(45)"/>
      <!-- product stage: photo of connectors -->
      <g role="img" aria-label="Foto: schwarze Solarstecker, Y-Verteiler und Kabelverbinder auf weißem Grund">
        <rect x="-210" y="-210" width="420" height="420" rx="30" fill="url(#product-tone)"
              transform="translate(815 205) rotate(45)"/>
        <rect x="494" y="175" width="130" height="264" rx="20" fill="var(--product-dark)"/>
      </g>
      <!-- corner accent bottom right -->
      <rect x="-170" y="-170" width="340" height="340" rx="44" fill="var(--yellow)"
            transform="translate(1236 388) rotate(45)"/>
    </svg>

    <div class="banner__content">
      <h1 class="banner__title">MONTAGE <span class="banner__highlight">UND</span><br>ANSCHLUSS</h1>
      <p class="banner__text">Unser Zubehörsortiment ist auf die angebotenen Produkte perfekt abgestimmt. So finden Sie zu allen Bereichen passende Stecker, Kabel, Adapter, Halterungen, uvm.</p>
    </div>

    <a class="banner__button" href="#">
      <svg width="14" height="14" viewBox="0 0 14 14" aria-hidden="true">
        <circle cx="7" cy="7" r="7" fill="var(--ink)"/>
        <path d="M5.5 4.3 L9.8 7 L5.5 9.7 Z" fill="var(--yellow)"/>
      </svg>
      VIDEOVORSTELLUNG DER EINZELNEN PRODUKTE
    </a>
  </section>
</body>
</html>
```